kestrel solar flyer design

My company name is Kestrel solar, it is a home business that provides consultancy to households to identify their specific power requirements, design pv solar system that meets their needs and get them a minimum of three quotations from three different companies that fit into their budgets.
We do not represent specific product or company but we assist the customer to find the right product for them.
I chose the boomerang because I believe that investing your money in solar just like throwing a boomerang, it will get back to you soon.
I want simple and elegant design that focus on the idea that we have a different approach from other solar companies, our focus on identifying customer's needs rather than trying to sell certain products. So we work for the customer and we are not biased towards any supplier. We will not charge customer anything.
Updated Flyer contents:
Book a free consultation today
Are you keen to have a solar panel system but overwhelmed by sales people telling you what the best is for you?
Call us now and try a different approach.
Our four steps process:
1. Reduce your power demand by increasing your home’s energy efficiency.
2. Design a system that meets your demand.
3. Get you a minimum of three quotations from different suppliers to choose from that will best fit your budget.
4. Installation supervision.
Bonus
With every system installed you will get a free comprehensive 12 months energy saving action plan and quarterly follow up for your property.
Contact details and website address will be given to the final design
Updates
Target Market(s)
target market is middle class families. ages usually between 28-60.
Industry/Entity Type
Business
Look and feel
Each slider illustrates characteristics of the customer's brand and the style your logo design should communicate.

```html
<!DOCTYPE html>
<html lang="en">
<head>
<meta charset="utf-8">
<title>Kestrel Solar – Flyer</title>
<link href="https://fonts.googleapis.com/css2?family=Open+Sans:ital,wght@0,300;0,400;0,600;0,700;1,300;1,600;1,700&family=Roboto+Slab:wght@300;400&display=swap" rel="stylesheet">
<style>
  :root {
    --stage: #ececec;
    --paper: #ffffff;
    --paper-tint: #f1f1f2;
    --orange: #ee8420;
    --charcoal: #4a4a4c;
    --ink: #3d3d3f;
    --ink-soft: #66666a;
    --bonus-bg: #e4e4e6;
  }
  * { box-sizing: border-box; margin: 0; padding: 0; }
  html, body { width: 1200px; height: 800px; overflow: hidden; }
  body {
    background: var(--stage);
    font-family: "Open Sans", Arial, sans-serif;
    color: var(--ink);
    position: relative;
  }
  .flyer {
    position: absolute;
    left: 335px; top: 25px;
    width: 530px; height: 750px;
    background: linear-gradient(180deg, var(--paper) 0%, var(--paper-tint) 100%);
    box-shadow: 0 6px 24px rgba(0,0,0,.18);
    overflow: hidden;
  }
  .top-rule { position: absolute; left: 0; top: 0; width: 100%; height: 9px; background: var(--charcoal); }
  .brand {
    position: absolute; top: 38px; left: 0; width: 100%;
    text-align: center;
  }
  .brand-name {
    font-family: "Open Sans", Arial, sans-serif;
    font-weight: 600; font-size: 22px; color: var(--charcoal);
    letter-spacing: .3px;
  }
  .hero-photo {
    position: absolute; left: 60px; top: 90px; width: 410px; height: 182px;
    background: radial-gradient(ellipse at 50% 55%, #c9ccd2 0%, #dfe1e5 45%, rgba(255,255,255,0) 75%);
  }
  .cta-band {
    position: absolute; left: 0; top: 272px; width: 100%; height: 40px;
    background: var(--orange);
    font-family: "Roboto Slab", Georgia, serif; font-weight: 300;
    color: #fff; font-size: 21px; line-height: 40px; padding-left: 52px;
    letter-spacing: .3px;
  }
  .pitch {
    position: absolute; left: 52px; top: 330px; width: 440px;
    font-style: italic; font-weight: 300; font-size: 16px; line-height: 26px; color: var(--ink-soft);
  }
  .pitch strong { font-weight: 600; color: var(--ink); }
  .approach-band {
    position: absolute; left: 0; top: 426px; width: 100%; height: 34px;
    background: var(--charcoal); color: #fff;
    font-family: "Roboto Slab", Georgia, serif; font-weight: 400;
    font-size: 17px; line-height: 34px; padding-left: 52px;
  }
  .steps {
    position: absolute; left: 52px; top: 480px; width: 440px; list-style: none;
    font-size: 11.5px; line-height: 18px; color: var(--ink);
  }
  .steps li { display: flex; gap: 10px; margin-bottom: 9px; }
  .tick { flex: 0 0 14px; width: 14px; height: 14px; margin-top: 2px; }
  .bonus {
    position: absolute; left: 0; top: 632px; width: 100%; height: 70px;
    background: var(--bonus-bg);
    padding: 16px 52px 0;
    font-style: italic; font-weight: 600; font-size: 12px; line-height: 20px; color: var(--ink);
  }
  .contact-band {
    position: absolute; left: 0; top: 702px; width: 100%; height: 48px;
    background: var(--orange); color: #fff;
    text-align: center; font-size: 12px; line-height: 48px;
  }
</style>
</head>
<body>
  <article class="flyer">
    <div class="top-rule"></div>

    <header class="brand">
      <span class="brand-name">Kestrel Solar</span>
    </header>

    <div class="hero-photo" role="img" aria-label="Top-down photo of engineers in hard hats around a table with plans and a solar panel"></div>

    <h1 class="cta-band">BOOK A FREE CONSULTATION TODAY</h1>

    <p class="pitch">Are you keen to have a <strong>solar panel system</strong> but<br>overwhelmed by sales people telling you<br><strong>what the best is for you?</strong></p>

    <h2 class="approach-band">Call us now and try a different approach.</h2>

    <ul class="steps">
      <li><svg class="tick" viewBox="0 0 14 14"><rect x="1" y="1" width="12" height="12" fill="none" stroke="#ee8420" stroke-width="1.5"/><path d="M3.5 7.2 6 9.6 11.5 3.6" fill="none" stroke="#ee8420" stroke-width="2"/></svg>Our four steps process:</li>
      <li><svg class="tick" viewBox="0 0 14 14"><rect x="1" y="1" width="12" height="12" fill="none" stroke="#ee8420" stroke-width="1.5"/><path d="M3.5 7.2 6 9.6 11.5 3.6" fill="none" stroke="#ee8420" stroke-width="2"/></svg>Reduce your power demand by increasing your home's energy efficiency.</li>
      <li><svg class="tick" viewBox="0 0 14 14"><rect x="1" y="1" width="12" height="12" fill="none" stroke="#ee8420" stroke-width="1.5"/><path d="M3.5 7.2 6 9.6 11.5 3.6" fill="none" stroke="#ee8420" stroke-width="2"/></svg>Design a system that meets your demand.</li>
      <li><svg class="tick" viewBox="0 0 14 14"><rect x="1" y="1" width="12" height="12" fill="none" stroke="#ee8420" stroke-width="1.5"/><path d="M3.5 7.2 6 9.6 11.5 3.6" fill="none" stroke="#ee8420" stroke-width="2"/></svg>Get you a minimum of three quotations from different suppliers to choose from that will best fit your budget.</li>
      <li><svg class="tick" viewBox="0 0 14 14"><rect x="1" y="1" width="12" height="12" fill="none" stroke="#ee8420" stroke-width="1.5"/><path d="M3.5 7.2 6 9.6 11.5 3.6" fill="none" stroke="#ee8420" stroke-width="2"/></svg>Installation supervision.</li>
    </ul>

    <p class="bonus">With every system installed you will get a free comprehensive 12 months energy saving action plan and quarterly follow up for your property.</p>

    <footer class="contact-band">www.kestrel-solar.com &nbsp;/&nbsp; info@kestrel-solar.com</footer>
  </article>
</body>
</html>
```